Web-Design  für naturwissenschaflich-philosophische Institution
Web-Design für naturwissenschaflich-philosophische Institution
Zielgruppe
Es handelt sich um eine naturwissenschaflich-philosophische Institution. Besucher sind neben Natur- und Geisteswissenschaftlern auch interessierte Laien.
Kernthema der Seite ist alles rund um das Thema Zahlen, allerdings unter einem naturwissenschaftlich, philosophischen Aspekt. Nach einer grundsätzlichen Erklärung (Leitartikel 'Wohin Wolken wandern') baut die Seite sich auf aus zahreichen Beispielen/Beiträgen aus den unterschiedlichsten Fachbereichen, die scheinbar keinerlei Bezug zueinander haben, wie Mathematik, Geometrie einerseits und der großen Literatur einschließlich historischer und religiöser Schriften andererseits. Immer aber gibt es einen Bezug zu fraktal wachsenden Dreiecken.
Die Artikel sind meist populärwissenschaftlich formuliert. Es handelt sich nicht um esoterische Inhalte, auch wenn der Domainname www.kornfeldwerk.de das evtl. vermuten ließe. Keine Berührung zu Spiritualität. Die Institution ist im Aufbau und hat durchaus den Anspruch, diese klassischen Themen modern aufzugreifen. Sie ist nicht verstaubt.
Aufgabenstellung
Geordneter, klarer, transparenter Aufbau. Übersichtlich und strukturiert, wie zB www.vkr-beispiel.de Es sollten geometrische Proportionen eingehalten werden (wie Symmetrie, goldener Schnitt). Nicht zu viele verschiedene Stilelemente. Die Seite sollte einladend sein, ggf. ansprechendes Bild auf Startseite (mit Bezug zu Zahlen, Geoemetrie).
Die Startseite braucht nun im Header kein Logo mehr zu haben. Der Seitentitel sollte sein 'Das Gewebe der Stille'. Siehe Anhang 'Header Beispiel'
Als Menüpunkte benötigen wir neben Home, nur 'Beiträge', 'Buch', 'Kontakt' oder einfach nur die bekannten drei Striche. Der Link zum Impressum genügt im Footer. Rechts oben benötigt man ein Suchfeld.
Besonderheit: Man benötigt eine Art zweiten Header, der aus einer Zahlenreihe besteht. Die einzelnen Zahlen müssen später verlinkt sein auf Unterseiten. Siehe Muster im Anhang. Der User muss sie als Link erkennen können (evtl. Programmierthema: zB Hervorheben beim drüberhoovern). Die Zahlen müssen erweiterbar sein, ggf. über Pfeil klicken, siehe
Es gibt einen zentralen Startartikel. Auf diesen muss man leicht kommen. Im Muster heißt er 'Wohin die Wolken wandern'.
Das Bild hier ist sehr wichtig. Es sollte bestehn aus vielen interessanten Zahlen, wie in 'Zahlenwolke' angegeben. Und möglichst auch den Dreiecken wie in 'Logo1'.
Weiter unten auf der Startseite sollte es dann weitere Elemente geben, einmal wo man zu bestimmten Unterkategorien kommt, im Muster sind das 'Bibel und Zahlen' 'Naturwissenschaft' etc. und dann evtl weiter unten noch ein Stilelemente, in welchem man die neuesten Artikel verlinken kann.

```html
<!DOCTYPE html>
<html lang="de">
<head>
<meta charset="utf-8">
<title>Das Gewebe der Stille</title>
<link href="https://fonts.googleapis.com/css2?family=Roboto:wght@300;400;500;700&display=swap" rel="stylesheet">
<style>
:root{
  --blue:#043795;
  --navy:#0b1a45;
  --ink:#1b2342;
  --rule:#5d6680;
  --card:#cbd6ea;
  --white:#ffffff;
}
*{box-sizing:border-box;margin:0;padding:0}
html,body{width:1094px;height:1200px;overflow:hidden;background:var(--white)}
body{position:relative;font-family:"Roboto",Arial,sans-serif;color:var(--ink)}
.abs{position:absolute}

/* header */
.brand-mark{left:167px;top:92px;width:30px;height:30px;background:var(--blue)}
.site-title{left:249px;top:93px;font-size:24px;font-weight:400;color:var(--navy);white-space:nowrap}
.main-nav a{position:absolute;top:106px;font-size:10px;font-weight:700;letter-spacing:2px;color:var(--navy);text-decoration:none}
.search{left:632px;top:152px;width:308px;height:30px;border-bottom:1px solid var(--rule)}
.search-btn{position:absolute;right:0;top:0;width:29px;height:30px;background:var(--navy)}

/* number series */
.series-label{left:502px;top:210px;font-size:13px;font-weight:300;color:var(--ink)}
.series{left:477px;top:233px;width:463px;height:27px;border-top:1px solid var(--rule);border-bottom:1px solid var(--rule)}
.series .arrow{position:absolute;top:-1px;width:25px;height:27px;background:var(--navy)}
.series .prev{left:0}.series .next{right:0}
.series a{position:absolute;top:7px;font-size:8.5px;font-weight:700;color:var(--navy);text-decoration:none;width:12px;text-align:center}

/* lead article */
.lead-ornament{left:158px;top:209px;width:165px;height:51px;background:linear-gradient(90deg,#0b1a45 0%,#1d3f8f 55%,rgba(4,55,149,.35) 100%)}
.lead{left:158px;top:260px;width:319px;height:90px;background:var(--blue)}
.lead-title{position:absolute;left:16px;top:16px;font-size:13px;font-weight:300;color:var(--white);white-space:nowrap}
.number-cloud{position:absolute;right:0;top:0;width:135px;height:90px;background:linear-gradient(135deg,#1a47a6 0%,#043795 60%,#0b1a45 100%)}
.lead-rule{left:477px;top:349px;width:463px;border-top:1px solid var(--rule)}

/* categories */
.rule{left:159px;width:781px;border-top:1px solid var(--rule)}
.cat-title{top:426px;font-size:13px;font-weight:400;color:var(--navy)}
.cat-photo{top:456px;width:228px;height:210px}
.photo-bible{background:linear-gradient(120deg,#5a2410 0%,#1a1f33 45%,#23283f 70%,#8aa07a 100%)}
.photo-science{background:radial-gradient(circle at 55% 35%,#d9a595 0%,#3a66b0 25%,#12306a 60%,#081a3d 100%)}
.photo-philo{background:linear-gradient(180deg,#9cb8dc 0%,#c9d8ea 30%,#4f5966 55%,#2f3640 100%)}

/* latest articles */
.card{top:737px;width:148px;height:226px;background:var(--card)}
.card-head{height:60px;background:var(--blue);color:var(--white);padding:10px 9px}
.card-head h3{font-size:10.5px;font-weight:300}
.card-head .name{font-size:7.5px;margin-top:3px}
.card-head .date{font-size:6.5px;letter-spacing:1px;margin-top:4px}
.card-body{padding:25px 14px 0 14px;font-size:9.6px;line-height:12.6px;color:var(--ink)}

/* footer */
.footer-rule{left:158px;top:1034px;width:782px;border-top:1px solid var(--navy)}
.footer-col{font-size:6.8px;letter-spacing:1.6px;color:var(--blue);text-transform:uppercase}
.footer-address{left:178px;top:1063px;line-height:14.4px}
.footer-col a{position:absolute;left:0;white-space:nowrap;color:var(--blue);text-decoration:none}
.footer-end{left:158px;top:1198px;width:782px;border-top:1px solid var(--navy)}
</style>
</head>
<body>

<header>
  <div class="abs brand-mark"></div>
  <h1 class="abs site-title">Das Gewebe der Stille</h1>
  <nav class="main-nav">
    <a href="#" style="left:632px">BEITRÄGE</a>
    <a href="#" style="left:769px">BUCH</a>
    <a href="#" style="left:886px">KONTAKT</a>
  </nav>
  <div class="abs search">
    <div class="search-btn">
      <svg width="29" height="30" viewBox="0 0 29 30"><circle cx="14" cy="13" r="8" fill="none" stroke="#fff" stroke-width="1"/><line x1="19.5" y1="18.5" x2="28" y2="28" stroke="#fff" stroke-width="1"/></svg>
    </div>
  </div>
</header>

<section>
  <p class="abs series-label">Was Zahlen erzählen …</p>
  <div class="abs series">
    <div class="arrow prev"><svg width="25" height="27"><polyline points="15,8 10,13.5 15,19" fill="none" stroke="#fff" stroke-width="1"/></svg></div>
    <a href="#" style="left:59px">1</a>
    <a href="#" style="left:105px">2</a>
    <a href="#" style="left:152px">3</a>
    <a href="#" style="left:198px">4</a>
    <a href="#" style="left:245px">5</a>
    <a href="#" style="left:291px">6</a>
    <a href="#" style="left:337px">7</a>
    <a href="#" style="left:383px">8</a>
    <div class="arrow next"><svg width="25" height="27"><polyline points="10,8 15,13.5 10,19" fill="none" stroke="#fff" stroke-width="1"/></svg></div>
  </div>

  <div class="abs lead-ornament" role="img" aria-label="Band aus wachsenden Dreiecken in Blau und Dunkelblau"></div>
  <article class="abs lead">
    <h2 class="lead-title">Wohin die Wolken wandern …</h2>
    <div class="number-cloud" role="img" aria-label="Zahlenwolke mit Zahlen, Formelzeichen und Dreiecken"></div>
  </article>
  <div class="abs lead-rule"></div>
</section>

<section>
  <div class="abs rule" style="top:413px"></div>
  <h2 class="abs cat-title" style="left:199px">Bibel und Zahlen</h2>
  <h2 class="abs cat-title" style="left:435px">Naturwissenschaft</h2>
  <h2 class="abs cat-title" style="left:673px">Philosophie</h2>
  <div class="abs cat-photo photo-bible" style="left:199px" role="img" aria-label="Foto einer schwarzen Bibel auf einem Tisch"></div>
  <div class="abs cat-photo photo-science" style="left:435px" role="img" aria-label="Foto einer leuchtenden DNA-Doppelhelix mit Molekülstrukturen"></div>
  <div class="abs cat-photo photo-philo" style="left:673px" role="img" aria-label="Foto eines Bücherstapels vor Wolkenhimmel"></div>
  <div class="abs rule" style="top:666px"></div>
</section>

<section>
  <article class="abs card" style="left:160px"><div class="card-head"><h3>Überschrift</h3><p class="name">Name</p><p class="date">XX.XX.XXXX</p></div><p class="card-body">Lorem ipsum dolor sit amet, consetetur sadipscing elitr, sed diam nonumy eirmod tempor invidunt ut labore et dolore magna aliquyam erat, sed diam voluptua. At vero eos et accusam et justo duo dolores et ea rebum.rat,</p></article>
  <article class="abs card" style="left:317px"><div class="card-head"><h3>Überschrift</h3><p class="name">Name</p><p class="date">XX.XX.XXXX</p></div><p class="card-body">Lorem ipsum dolor sit amet, consetetur sadipscing elitr, sed diam nonumy eirmod tempor invidunt ut labore et dolore magna aliquyam erat, sed diam voluptua. At vero eos et accusam et justo duo dolores et ea rebum.rat,</p></article>
  <article class="abs card" style="left:474px"><div class="card-head"><h3>Überschrift</h3><p class="name">Name</p><p class="date">XX.XX.XXXX</p></div><p class="card-body">Lorem ipsum dolor sit amet, consetetur sadipscing elitr, sed diam nonumy eirmod tempor invidunt ut labore et dolore magna aliquyam erat, sed diam voluptua. At vero eos et accusam et justo duo dolores et ea rebum.rat,</p></article>
  <article class="abs card" style="left:633px"><div class="card-head"><h3>Überschrift</h3><p class="name">Name</p><p class="date">XX.XX.XXXX</p></div><p class="card-body">Lorem ipsum dolor sit amet, consetetur sadipscing elitr, sed diam nonumy eirmod tempor invidunt ut labore et dolore magna aliquyam erat, sed diam voluptua. At vero eos et accusam et justo duo dolores et ea rebum.rat,</p></article>
  <article class="abs card" style="left:791px"><div class="card-head"><h3>Überschrift</h3><p class="name">Name</p><p class="date">XX.XX.XXXX</p></div><p class="card-body">Lorem ipsum dolor sit amet, consetetur sadipscing elitr, sed diam nonumy eirmod tempor invidunt ut labore et dolore magna aliquyam erat, sed diam voluptua. At vero eos et accusam et justo duo dolores et ea rebum.rat,</p></article>
</section>

<footer>
  <div class="abs footer-rule"></div>
  <address class="abs footer-col footer-address" style="font-style:normal">
    Kornfeldwerk<br>
    Naturwissenschaftlich-<br>
    philosophische Institution<br>
    Musterstraße 1a<br>
    12345 Musterstadt<br>
    E-Mail: info@kornfeldwerk.de<br>
    Tel.:&nbsp; 012 1234 5678
  </address>
  <nav class="abs footer-col" style="left:443px;top:1063px">
    <a href="#" style="top:0">Beiträge</a>
    <a href="#" style="top:26px">Buch</a>
    <a href="#" style="top:52px">Kontakt</a>
  </nav>
  <nav class="abs footer-col" style="left:659px;top:1063px">
    <a href="#" style="top:0">Impressum</a>
    <a href="#" style="top:32px">Haftungsausschluss</a>
    <a href="#" style="top:63px">Datenschutzerklärung</a>
  </nav>
  <div class="abs footer-end"></div>
</footer>

</body>
</html>
```